ONE PAGE WEB DESIGN NEEDED for Finance Company

We need a web design (ONE PAGE DESIGN ONLY) for a new finance website called Brightwell Lending. Brightwell Lending helps customers get the right loan, whether its a home loan, investment loan, business loan etc.

You are required to come up with just the homepage design. Professionalism and quality is the key factors in the successful design.

Here are a few design questions to help you out:

-
What information should be used on the page?
Ive provided a document which outlines all the information needed to put on homepage (attached to the brief - called brightwell_page_info). Also see the Must Have section below on this brief.

-
What links should appear in the navigation/footer?:
The navigation should provide links to the following pages (NOTE: services link has subcategories):
1 Homepage
2 Services
- Home loans
- Investment loans
- Refinancing loans
- Business loans
3 About Us
4 FAQ
5 Contact Us

-
What colors should be used in the design?
Our company colors - Cyan: #2EADE3, Blue: #004B70, White. Feel free to submit designs with slight variations if you feel it improves the design.

-
What should the layout of the page be?
This is up to you to come up with - we are open to different layouts for the page design (as long as they capture the information effectively and making it easy to understand).

Target Market(s)

Potential Home owners, Families and Business Owners

Industry/Entity Type

Business

Requirements
Must have
• - Must contain our logo (attached as PNG and Illustrator file)
- Winning designer must supply a Photoshop file (PSD) that will allow us.
Nice to have
• - Should include photos/images of families, professional groups, tradespeople etc (you can use stock photos from PixQuarry and I will purchase them once you are selected as the winning design)
- Link to a loan calculator somewhere on front page with a button 'Find out how much you could borrow' (or maybe even try adding a loan calculator to the homepage if you think this would look good)
- Page should have a main headline "Finding the right loan for you" or "Brightwell Lending finds the right loan for our customers."
- Must include Accreditation logos somewhere on the homepage (will try and supply these soon)
Should not have
• - Poor quality designs will not be considered
- Do not use clipart

```html
<!DOCTYPE html>
<html lang="en">
<head>
<meta charset="utf-8">
<title>Brightwell Lending – Finding the Right Loan For You</title>
<link href="https://fonts.googleapis.com/css2?family=Ubuntu:wght@400;500;700&family=Open+Sans:wght@400;600&display=swap" rel="stylesheet">
<style>
:root{
  --cyan:#2eade3;
  --cyan-deep:#0b8fc6;
  --blue:#004b70;
  --blue-mid:#1a6fa3;
  --ink:#222;
  --text:#333;
  --muted:#666;
  --panel:#f2f2f2;
  --line:#cfcfcf;
  --footer:#555;
  --footer-text:#ddd;
  --white:#fff;
}
*{box-sizing:border-box;margin:0;padding:0}
html,body{width:950px;height:1200px;overflow:hidden;background:var(--white)}
body{position:relative;font-family:"Open Sans",Arial,sans-serif;color:var(--text)}
.abs{position:absolute}
a{color:inherit;text-decoration:none}

/* header */
.brand{left:110px;top:20px;display:flex;align-items:center;gap:8px}
.brand-mark{width:26px;height:26px;border-radius:50%;background:var(--cyan)}
.brand-name{font-family:"Ubuntu",sans-serif;font-weight:500;font-size:22px;color:var(--blue-mid);letter-spacing:-.3px}
.contact-line{right:114px;top:31px;display:flex;align-items:center;gap:8px;font-family:"Ubuntu",sans-serif;color:var(--blue-mid);font-size:14px}
.contact-line .phone{font-size:12px}
.main-nav{left:336px;top:59px;width:503px;height:38px;border-radius:3px;background:linear-gradient(#2a8fc4,#135f8f);display:flex;align-items:center;justify-content:space-around;font-family:"Ubuntu",sans-serif;font-weight:500;font-size:12.5px;color:var(--white)}
.main-nav span{display:flex;align-items:center;gap:6px}

/* hero */
.hero-frame{left:94px;top:120px;width:751px;height:287px;border:1px solid var(--line);background:var(--white)}
.hero-shadow{left:94px;top:407px;width:753px;height:14px;background:linear-gradient(#e4e4e4,rgba(255,255,255,0))}
.hero{left:111px;top:134px;width:719px;height:256px;background:linear-gradient(90deg,#f2f1f1 0%,#efedec 40%,#e8e2dc 100%);border:1px solid #e2e2e2;overflow:hidden}
.hero-photo{position:absolute;left:345px;top:0;width:374px;height:256px;background:linear-gradient(90deg,rgba(239,236,233,0) 0%,#d9c9b8 30%,#c8a98d 60%,#b8a49a 100%)}
.hero h1{position:absolute;left:27px;top:27px;font-family:"Ubuntu",sans-serif;font-weight:400;font-size:29px;line-height:33px;color:#444}
.hero h1 b{font-weight:700;color:#3a3a3a}
.hero p{position:absolute;left:28px;top:102px;width:300px;font-size:10.5px;line-height:18.5px;color:var(--ink)}
.btn-more{position:absolute;left:28px;top:170px;width:111px;height:34px;border-radius:3px;background:linear-gradient(#2a8fc4,#156798);color:var(--white);font-family:"Ubuntu",sans-serif;font-size:15px;display:flex;align-items:center;justify-content:center}
.dots{position:absolute;left:33px;top:219px;display:flex;gap:6px}
.dots i{width:8px;height:8px;border-radius:50%;background:#111}
.dots i:first-child{background:var(--blue-mid)}

/* service cards */
.card{top:434px;width:177px;height:167px;border:1px solid #d6d6d6;background:linear-gradient(#f6f6f6,#e9e9e9)}
.card h2{height:44px;background:linear-gradient(var(--cyan-deep),#1492c8);color:var(--white);font-family:"Ubuntu",sans-serif;font-weight:400;font-size:19px;padding:10px 0 0 14px;margin:-1px -1px 0 -1px}
.card ul{list-style:none;padding:18px 0 0 10px}
.card li{font-size:9.5px;line-height:12.5px;color:#444;text-decoration:underline;display:flex;gap:7px;margin-bottom:7px}
.card li svg{flex:none;margin-top:2px}
.card .more{position:absolute;left:25px;bottom:10px;font-size:10px;color:var(--ink)}

/* welcome */
.welcome{left:107px;top:628px;width:440px}
.welcome h2{font-family:"Ubuntu",sans-serif;font-weight:400;font-size:22.5px;color:var(--ink);margin-bottom:14px}
.welcome h2 span{color:var(--blue-mid)}
.welcome p{font-size:11.5px;line-height:16.5px;color:var(--text);margin-bottom:16px;padding-left:2px}

/* calculator */
.calc{left:589px;top:628px;width:240px;font-size:11.5px;color:var(--ink)}
.calc h2{font-family:"Ubuntu",sans-serif;font-weight:400;font-size:22.5px;color:var(--ink);margin-bottom:14px}
.calc-row{position:relative;height:31px}
.calc-row label{position:absolute;left:1px;top:4px}
.field{position:absolute;left:81px;top:2px;width:156px;height:17px;border:1px solid #bbb;background:linear-gradient(#f3f3f3,#fff)}
.slider{position:absolute;left:81px;top:8px;width:80px;height:7px;border-radius:4px;border:1px solid #bbb;background:#f3f3f3}
.slider i{position:absolute;left:31px;top:-4px;width:13px;height:13px;border-radius:50%;border:1px solid #aaa;background:#fff}
.slider i::after{content:"";position:absolute;left:4px;top:4px;width:3px;height:3px;border-radius:50%;background:var(--blue-mid)}
.years-box{position:absolute;left:171px;top:1px;width:34px;height:18px;border:1px solid #bbb;font-size:10.5px;padding:1px 0 0 5px}
.years{position:absolute;left:212px;top:4px;font-size:10px;color:var(--muted)}
.radio{position:absolute;left:87px;font-size:9.5px;color:var(--muted);display:flex;align-items:center;gap:5px}
.radio i{width:9px;height:9px;border-radius:50%;border:1px solid #888;position:relative}
.radio i.on::after{content:"";position:absolute;left:2px;top:2px;width:3px;height:3px;border-radius:50%;background:#3a9a3a}
.btn-calc{position:absolute;left:71px;top:178px;width:83px;height:25px;border-radius:2px;background:linear-gradient(#2a8fc4,#156798);color:var(--white);font-family:"Ubuntu",sans-serif;font-size:13px;display:flex;align-items:center;justify-content:center}

/* clients */
.clients-rule{left:102px;top:873px;width:733px;height:1px;background:#ccc}
.clients-title{left:418px;top:862px;padding:0 12px;background:var(--white);font-family:"Ubuntu",sans-serif;font-size:16px;color:#555}
.clients{left:106px;top:902px;width:730px;display:flex;justify-content:space-between;align-items:center}
.client{display:flex;align-items:center;gap:5px;font-family:"Ubuntu",sans-serif;font-size:15px;color:#555}
.client i{width:12px;height:12px;border-radius:50%;background:#9aa7b3}

/* footer */
.site-footer{left:95px;top:968px;width:782px;height:182px;background:var(--footer);color:var(--footer-text)}
.foot-col{position:absolute;top:17px}
.foot-col h3{font-family:"Ubuntu",sans-serif;font-weight:400;font-size:16px;color:var(--white);margin-bottom:13px}
.foot-col p,.foot-col li{font-size:9.5px;line-height:15px}
.foot-col ul{list-style:none;padding-left:2px}
.follow li{display:flex;align-items:center;gap:9px;height:27.5px}
.follow li i{width:19px;height:19px;border-radius:50%;background:var(--cyan)}
.copyright{left:95px;top:1150px;width:782px;height:38px;background:linear-gradient(#eee,#fff);border:1px solid #ddd;border-top:0;font-size:8.5px;font-weight:600;color:var(--ink);display:flex;align-items:center;padding-left:145px}
</style>
</head>
<body>

<header>
  <div class="abs brand"><span class="brand-mark"></span><span class="brand-name">brightwelllending</span></div>
  <div class="abs contact-line">
    <span>Contact Brightwell Lending today:</span>
    <svg width="24" height="24" viewBox="0 0 24 24" aria-hidden="true"><circle cx="12" cy="12" r="11" fill="none" stroke="#222" stroke-width="1.6"/><path d="M8 6.5c-1 1-1 3 1 6s4.5 5 6 5l1.7-1.7-2.3-2-1.3 1c-1-.5-2.6-2.2-3-3.2l1-1.3-2-2.3z" fill="#222"/></svg>
    <span class="phone">1800-555-210</span>
  </div>
  <nav class="abs main-nav">
    <span>Homepage</span>
    <span>Services <svg width="8" height="6" viewBox="0 0 8 6"><path d="M1 1l3 3 3-3" fill="none" stroke="#fff" stroke-width="1.8"/></svg></span>
    <span>About Us</span>
    <span>Faq</span>
    <span>Contact Us</span>
  </nav>
</header>

<div class="abs hero-frame"></div>
<div class="abs hero-shadow"></div>
<section class="abs hero">
  <div class="hero-photo" role="img" aria-label="Stock photo of a smiling family of five posing together"></div>
  <h1>Finding the Right <b>Loan</b><br>For <b>You</b></h1>
  <p>Lorem Ipsum is simply dummy text of the printing and typesetting industry. Lorem Ipsum has been the industry's standard dummy text ever since the 1500s, when an......</p>
  <a class="btn-more">Read More</a>
  <div class="dots"><i></i><i></i><i></i></div>
</section>

<section>
  <div class="abs card" style="left:97px">
    <h2>Home Loan</h2>
    <ul>
      <li><svg width="8" height="7" viewBox="0 0 8 7"><path d="M1 4l2 2 4-5" fill="none" stroke="#1a6fa3" stroke-width="1.6"/></svg>Home buyers</li>
      <li><svg width="8" height="7" viewBox="0 0 8 7"><path d="M1 4l2 2 4-5" fill="none" stroke="#1a6fa3" stroke-width="1.6"/></svg>First home buyers</li>
      <li><svg width="8" height="7" viewBox="0 0 8 7"><path d="M1 4l2 2 4-5" fill="none" stroke="#1a6fa3" stroke-width="1.6"/></svg>Over 20 lenders</li>
    </ul>
    <span class="more">More</span>
  </div>
  <div class="abs card" style="left:286px">
    <h2>Investment Loan</h2>
    <ul>
      <li><svg width="8" height="7" viewBox="0 0 8 7"><path d="M1 4l2 2 4-5" fill="none" stroke="#1a6fa3" stroke-width="1.6"/></svg>Property investment</li>
      <li><svg width="8" height="7" viewBox="0 0 8 7"><path d="M1 4l2 2 4-5" fill="none" stroke="#1a6fa3" stroke-width="1.6"/></svg>Interest only loans</li>
    </ul>
    <span class="more">More</span>
  </div>
  <div class="abs card" style="left:476px">
    <h2>Refinancing</h2>
    <ul>
      <li><svg width="8" height="7" viewBox="0 0 8 7"><path d="M1 4l2 2 4-5" fill="none" stroke="#1a6fa3" stroke-width="1.6"/></svg>Refinancing for the best rate</li>
      <li><svg width="8" height="7" viewBox="0 0 8 7"><path d="M1 4l2 2 4-5" fill="none" stroke="#1a6fa3" stroke-width="1.6"/></svg>Upsizing or downsizing</li>
      <li><svg width="8" height="7" viewBox="0 0 8 7"><path d="M1 4l2 2 4-5" fill="none" stroke="#1a6fa3" stroke-width="1.6"/></svg>Change from a variable to a<br>fixed rate</li>
    </ul>
    <span class="more">More</span>
  </div>
  <div class="abs card" style="left:666px">
    <h2>Business Loan</h2>
    <ul>
      <li><svg width="8" height="7" viewBox="0 0 8 7"><path d="M1 4l2 2 4-5" fill="none" stroke="#1a6fa3" stroke-width="1.6"/></svg>Long term</li>
      <li><svg width="8" height="7" viewBox="0 0 8 7"><path d="M1 4l2 2 4-5" fill="none" stroke="#1a6fa3" stroke-width="1.6"/></svg>Short term</li>
      <li><svg width="8" height="7" viewBox="0 0 8 7"><path d="M1 4l2 2 4-5" fill="none" stroke="#1a6fa3" stroke-width="1.6"/></svg>Equipment and Leasing</li>
    </ul>
    <span class="more">More</span>
  </div>
</section>

<section class="abs welcome">
  <h2>Welcome to <span>Brightwell Lending</span></h2>
  <p>At Brightwell Lending we work hard to find the right loan for our customers. We do that because we are backed by sound industry knowledge, professional experience and a great customer service approach.</p>
  <p>Brightwell Lending guarantees that we will always tailor the best solution for your individual lending needs.</p>
  <p>We can do that because we have access to a wide variety of lending options from major banks to non-bank lenders and we are committed to finding the right lending product for you.</p>
</section>

<section class="abs calc">
  <h2>Loan Calculator</h2>
  <div class="calc-row"><label>Loan amount</label><span class="field"></span></div>
  <div class="calc-row"><label>Interest rate:</label><span class="field"></span></div>
  <div class="calc-row"><label>Loan period:</label><span class="slider"><i></i></span><span class="years-box">25</span><span class="years">years</span></div>
  <div class="calc-row" style="height:46px"><label>Amortization:</label>
    <span class="radio" style="top:6px"><i class="on"></i>show by month</span>
    <span class="radio" style="top:24px"><i></i>show by year</span>
  </div>
  <a class="btn-calc">calculate</a>
</section>

<div class="abs clients-rule"></div>
<div class="abs clients-title">Our Clients</div>
<div class="abs clients">
  <span class="client"><i></i>Corvix</span>
  <span class="client"><i></i>Nodeway</span>
  <span class="client"><i></i>Shopvale</span>
  <span class="client"><i></i>Tradeloom</span>
  <span class="client"><i></i>Pressfield</span>
  <span class="client"><i></i>Dropleaf</span>
  <span class="client"><i></i>Kettle</span>
</div>

<footer class="abs site-footer">
  <div class="foot-col" style="left:29px">
    <h3>About Us</h3>
    <ul><li>Homepage</li><li>Services</li><li>About Us</li><li>Faq</li><li>Contact Us</li></ul>
  </div>
  <div class="foot-col" style="left:178px;width:165px">
    <h3>Information</h3>
    <p>At Brightwell Lending we work hard to find the right loan for our customers. We do that because we are backed by sound industry knowledge, professional experience and a great customer service approach.</p>
  </div>
  <div class="foot-col follow" style="left:380px">
    <h3>Follow Us</h3>
    <ul style="margin-top:-5px">
      <li><i></i>Follow us on Friendspace</li>
      <li><i></i>Follow us on Chirpline</li>
      <li><i></i>Follow us on Workcircle</li>
      <li><i style="background:#f08a24"></i>Follow us on Rss</li>
    </ul>
  </div>
  <div class="foot-col" style="left:558px;width:170px">
    <h3>Others</h3>
    <p>Brightwell Lending guarantees that we will always tailor the best solution for your individual lending needs.</p>
  </div>
</footer>
<div class="abs copyright">COPYRIGHT - include a copyright statement © 2012 Brightwell Lending. | All rights reserved.</div>

</body>
</html>
```